Marketing Flyer for Plumber Referals

8.5" x11" Layout should be landscape not portrait. Create a bold, eye-catching flyer that highlights earning potential from referrals for water damage restoration. Use high-contrast colors like blue, yellow, and white, with bold fonts and dynamic layouts. Include images of restoration work, cash, and happy clients. Emphasize key benefits like $500 minimum payouts, fast payments, and unlimited income potential. Keep instructions simple: refer a client, we handle the work, you get paid. Add a clear call-to-action and display contact details prominently. Focus on professionalism and energy.

Target Market(s)

Plumbers and Contractor 8.5" x11" Layout should be landscape not portrait.

Industry/Entity Type

General Contractor

Colors
0054AA
0677BA
7BADD7
CADEEF
E8F1F8
EB3D1F
EC4F4E
F09395
F8D3D4
FCEDEE

Requirements
Must have
• 8.5" x11" Layout should be landscape not portrait.
Nice to have

```html
<!DOCTYPE html>
<html lang="en">
<head>
<meta charset="utf-8">
<title>Harborline Remodel – Flood Referral Flyer</title>
<link rel="stylesheet" href="https://fonts.googleapis.com/css2?family=Archivo:wdth,wght@62..125,100..900&family=Poppins:wght@400;500;600;700;800&display=swap">
<style>
:root{
  --stage:#646464;
  --ink:#141518;
  --blue:#0054AA;
  --blue-mid:#0677BA;
  --navy:#0b3a78;
  --navy-deep:#061a3a;
  --sky:#CADEEF;
  --red:#EB3D1F;
  --yellow:#FFC400;
  --white:#ffffff;
}
*{box-sizing:border-box;margin:0;padding:0}
html,body{width:728px;height:1200px;overflow:hidden}
body{background:var(--stage);position:relative;font-family:"Poppins",sans-serif;color:var(--white)}
.side{position:absolute;left:59px;width:610px;height:470px;overflow:hidden;background:var(--ink)}
.side--front{top:116px}
.side--back{top:604px}
.abs{position:absolute}
.shapes{position:absolute;inset:0;width:610px;height:470px}
.display{font-family:"Archivo",sans-serif;font-stretch:125%;font-weight:900;line-height:1;letter-spacing:-.5px;white-space:nowrap;transform-origin:left top}

/* front */
.hero-photo{position:absolute;left:0;top:0;width:610px;height:300px;
  background:linear-gradient(90deg,#141518 0%,#1c1d21 30%,#4a4c52 55%,#b9bcc2 78%,#d8dadd 100%)}
.brand{left:30px;top:44px;width:136px;text-align:center}
.brand__mark{width:14px;height:14px;border-radius:50%;border:1.5px solid var(--white);margin:0 auto 6px}
.brand__name{font-size:11px;font-weight:500;letter-spacing:.3px;line-height:1.1;white-space:nowrap}
.brand__tag{font-size:5.5px;letter-spacing:1.2px;margin-top:2px;white-space:nowrap;line-height:1.2}
.headline--earn,.headline--unlimited,.headline--cash{font-size:43px;transform:scaleX(1.2)}
.headline--earn{left:29px;top:104px;color:var(--white)}
.headline--unlimited{left:29px;top:141px;color:var(--red)}
.headline--cash{left:29px;top:178px;color:var(--blue-mid)}
.headline-sub{left:30px;top:213px;font-size:22px;font-weight:400;letter-spacing:-.3px;color:var(--white);white-space:nowrap}
.headline-sub b{font-weight:700;color:var(--sky)}
.benefits{left:30px;top:268px;width:330px}
.benefits__title{font-size:13.5px;font-weight:800;line-height:1.12;margin-bottom:4px}
.benefit{position:relative;padding-left:13px;margin-bottom:3px}
.benefit svg{position:absolute;left:0;top:2px;width:9px;height:9px}
.benefit__head{font-size:12px;font-weight:800;color:var(--yellow);line-height:1.05;letter-spacing:.2px}
.benefit__text{font-size:11.2px;line-height:1.02;letter-spacing:.2px}
.payout{right:30px;top:292px;text-align:right}
.payout__amount{font-size:41px;font-weight:800;line-height:1;color:var(--white)}
.payout__min{font-size:40px;font-weight:800;line-height:.95;color:var(--yellow);letter-spacing:-.5px}
.payout__pct{font-size:40px;font-weight:800;line-height:1;color:var(--red);letter-spacing:-.5px}
.payout__pct span{font-size:24px;color:var(--white);margin-right:4px}
.payout__ref{font-size:24px;font-weight:800;line-height:1}
.band{left:0;bottom:0;width:610px;height:36px;background:var(--red);display:flex;align-items:center;justify-content:center;font-weight:700;white-space:nowrap}
.band--tagline{font-size:18px;letter-spacing:2.6px}
.band--web{font-size:18px;font-weight:500;letter-spacing:1px}

/* back */
.scene-photo{position:absolute;left:0;top:0;width:610px;height:300px;
  background:linear-gradient(90deg,#141518 0%,#1e2024 30%,#55585e 55%,#9a9ca1 75%,#c6c7ca 100%)}
.headline2{left:35px;font-size:40px;transform:scaleX(1.32)}
.headline2--a{top:30px}
.headline2--b{top:68px;color:var(--yellow)}
.headline2--c{top:105px}
.red{color:var(--red)}
.rule{left:26px;top:167px;width:558px;height:1px;background:#c9c9c9}
.pill{left:233px;top:153px;width:144px;height:29px;border-radius:15px;background:var(--navy-deep);border:1px solid var(--blue);display:flex;align-items:center;justify-content:center;font-size:14px;font-weight:700}
.steps{left:24px;top:188px;display:flex;gap:6px}
.step{width:183px}
.step__photo{height:89px}
.step__label{height:36px;background:var(--yellow);color:var(--ink);display:flex;align-items:center;justify-content:center;text-align:center;font-size:11px;font-weight:700;line-height:1.1;padding:0 8px}
.step__text{margin-top:5px;text-align:center;font-size:12px;line-height:1.17;letter-spacing:.2px}
.contact-cta{left:24px;top:392px;font-size:18.5px;font-weight:700;color:var(--yellow);white-space:nowrap}
.phone-number{left:325px;top:379px;font-size:36px;font-weight:800;color:var(--navy);letter-spacing:-.3px;white-space:nowrap}
</style>
</head>
<body>

<section class="side side--front">
  <div class="hero-photo" role="img" aria-label="Photo: leaking white drain pipe and an excited young man holding a fan of dollar bills"></div>
  <svg class="shapes" viewBox="0 0 610 470" aria-hidden="true">
    <polygon points="0,244 381,308 610,258 610,470 0,470" fill="var(--blue)"/>
    <polygon points="381,308 610,258 610,470 338,470" fill="var(--navy)"/>
    <polygon points="0,240 381,302 610,252 610,258 381,308 0,248" fill="var(--red)"/>
    <polygon points="0,238 381,296 610,248 610,252 381,302 0,240" fill="var(--white)"/>
  </svg>

  <div class="abs brand">
    <div class="brand__mark"></div>
    <div class="brand__name">HARBORLINE REMODEL</div>
    <div class="brand__tag">COASTAL QUALITY BUILDERS</div>
  </div>

  <div class="abs display headline--earn">EARN</div>
  <div class="abs display headline--unlimited">UNLIMITED</div>
  <div class="abs display headline--cash">CASH</div>
  <div class="abs headline-sub"><b>GET PAID</b> TO REFER A FLOOD</div>

  <div class="abs benefits">
    <div class="benefits__title">WHY<br>PARTNER WITH US?</div>
    <div class="benefit">
      <svg viewBox="0 0 10 10"><circle cx="5" cy="5" r="4.2" fill="none" stroke="#fff" stroke-width="1.1"/><path d="M3 5.1l1.4 1.4L7 3.8" fill="none" stroke="#fff" stroke-width="1.1"/></svg>
      <div class="benefit__head">GUARANTEED PAYOUT:</div>
      <div class="benefit__text">Minimum $500 or 10% of the invoice, paid fast.</div>
    </div>
    <div class="benefit">
      <svg viewBox="0 0 10 10"><circle cx="5" cy="5" r="4.2" fill="none" stroke="#fff" stroke-width="1.1"/><path d="M3 5.1l1.4 1.4L7 3.8" fill="none" stroke="#fff" stroke-width="1.1"/></svg>
      <div class="benefit__head">FREE EVALUATIONS:</div>
      <div class="benefit__text">We assess damage and process insurance claims for your clients.</div>
    </div>
    <div class="benefit">
      <svg viewBox="0 0 10 10"><circle cx="5" cy="5" r="4.2" fill="none" stroke="#fff" stroke-width="1.1"/><path d="M3 5.1l1.4 1.4L7 3.8" fill="none" stroke="#fff" stroke-width="1.1"/></svg>
      <div class="benefit__head">INDUSTRY LEADERS:</div>
      <div class="benefit__text">Certified experts with 24/7 rapid response.</div>
    </div>
    <div class="benefit">
      <svg viewBox="0 0 10 10"><circle cx="5" cy="5" r="4.2" fill="none" stroke="#fff" stroke-width="1.1"/><path d="M3 5.1l1.4 1.4L7 3.8" fill="none" stroke="#fff" stroke-width="1.1"/></svg>
      <div class="benefit__head">AFFORDABLE SOLUTIONS:</div>
      <div class="benefit__text">Lowest out-of-pocket costs for your customers.</div>
    </div>
  </div>

  <div class="abs payout">
    <div class="payout__amount">$500</div>
    <div class="payout__min">Minimum</div>
    <div class="payout__pct"><span>or</span>10% Per</div>
    <div class="payout__ref">Referral!</div>
  </div>

  <div class="abs band band--tagline">Send Referrals | Get Paid | Grow Your Business</div>
</section>

<section class="side side--back">
  <div class="scene-photo" role="img" aria-label="Photo: flooded hallway with water covering the floor at the foot of a staircase"></div>
  <svg class="shapes" viewBox="0 0 610 470" aria-hidden="true">
    <polygon points="0,236 270,236 610,290 610,470 0,470" fill="var(--navy)"/>
    <polygon points="0,265 610,300 610,470 0,470" fill="var(--navy)"/>
    <polygon points="305,374 610,374 610,434 288,434" fill="var(--white)"/>
    <circle cx="293" cy="404" r="24" fill="var(--navy)"/>
    <circle cx="293" cy="404" r="21" fill="var(--red)"/>
    <path d="M286 394c1.5-1 3-.8 3.6.6l1.4 3c.5 1-.1 1.9-.9 2.5l-.8.6c.9 2.2 2.6 4.2 4.6 5.4l.7-.8c.7-.8 1.7-1.2 2.6-.6l2.8 1.8c1.2.8 1.2 2.3.1 3.5-2.2 2.3-5.4 1.6-8.5-1-3.3-2.8-5.9-6.7-6.3-10-.3-2.3.6-4 .7-4z" fill="var(--white)"/>
    <path d="M295 393a8 8 0 0 1 7 7M295 389.5a11.5 11.5 0 0 1 10.5 10.5" fill="none" stroke="var(--white)" stroke-width="1.6" stroke-linecap="round"/>
  </svg>

  <div class="abs display headline2 headline2--a">GET <span class="red">PAID</span></div>
  <div class="abs display headline2 headline2--b">TO REFER</div>
  <div class="abs display headline2 headline2--c"><span class="red">A</span> FLOOD</div>

  <div class="abs rule"></div>
  <div class="abs pill">How It Works</div>

  <div class="abs steps">
    <div class="step">
      <div class="step__photo" role="img" aria-label="Photo collage: water-stained wall, torn drywall and a flooded kitchen" style="background:linear-gradient(90deg,#d9cfc2,#8a5a3c 50%,#e6e4df)"></div>
      <div class="step__label">REFER FLOOD, WATER AND MOLD DAMAGE</div>
      <div class="step__text">Call, book online, or text<br>us directly.</div>
    </div>
    <div class="step">
      <div class="step__photo" role="img" aria-label="Photo: contractor holding a work estimate clipboard in front of a brick house" style="background:linear-gradient(90deg,#4d86c0,#6d7f58 40%,#8a5040 70%,#cfd3d6)"></div>
      <div class="step__label">WE TAKE CARE OF EVERYTHING</div>
      <div class="step__text">Free evaluations,<br>insurance claims, and<br>professional service.</div>
    </div>
    <div class="step">
      <div class="step__photo" role="img" aria-label="Photo: spread of hundred-dollar bills with letter tiles spelling cash flow" style="background:linear-gradient(135deg,#e3e5dc,#b9c0b0 50%,#dfe3da)"></div>
      <div class="step__label">GET PAID FAST</div>
      <div class="step__text">$500 minimum or 10% of<br>the invoice within 48 hours<br>of final payment.</div>
    </div>
  </div>

  <div class="abs contact-cta">Call Text or Book On-line</div>
  <div class="abs phone-number">555-014-2290</div>

  <div class="abs band band--web">www.HarborlineRemodel.com</div>
</section>

</body>
</html>
```